We want to design total new business card and logo for Kestrel Building Services Ltd

Our company name Kestrel Building Services Ltd. Design new logo and business card , need hi-end luxury style art for architecture and construction industry. The card should simple but stylish. Our business focus on CONNECT tradesman to construction company, help marketing construction company tender oversea projects, managing franchise in construction sector, delivery amazing services to our client, so Logo should show the CONNECTION IDEA, CONNECTING PEOPLE, LUXURY. Visit our website for more information: kestrelhub.co.nz

Low design quality

Target Market(s)

Directors or managers

Industry/Entity Type

Construction Company

Contact Information for Business Card

Name, Title, Mobile, Email, Website

Font styles to use
Serif

Colors

Designer to choose colors to be used in the design.

Requirements
Must have
• Simple and luxury, connection icon
Nice to have
• Special materials, plastic card, look through,...
• Look new ideas.

```html
<!DOCTYPE html>
<html lang="en">
<head>
<meta charset="utf-8">
<title>Kestrel Building Services Ltd — Business Card</title>
<link href="https://fonts.googleapis.com/css2?family=Montserrat:wght@500;600&family=Work+Sans:wght@400;500&display=swap" rel="stylesheet">
<style>
  :root {
    --backdrop: #b9b9b9;
    --brand-blue: #0f57a8;
    --brand-blue-light: #2a6fbf;
    --card-white: #ffffff;
    --ink-grey: #555a60;
    --rule-blue: #1d5fb0;
    --icon-blue: #1d5fb0;
  }
  * { margin: 0; padding: 0; box-sizing: border-box; }
  html, body { width: 1200px; height: 930px; overflow: hidden; }
  body {
    background: var(--backdrop);
    position: relative;
    font-family: "Work Sans", sans-serif;
  }
  .card {
    position: absolute;
    width: 580px;
    height: 330px;
    border-radius: 22px;
    overflow: hidden;
  }
  /* Front */
  .card-front {
    left: 80px; top: 90px;
    background: linear-gradient(120deg, var(--brand-blue-light), var(--brand-blue) 55%);
    color: var(--card-white);
    display: flex; flex-direction: column; align-items: center; justify-content: center;
  }
  .front-mark {
    width: 54px; height: 54px; border-radius: 50%;
    background: var(--card-white);
    margin-bottom: 22px;
  }
  .front-name {
    font-family: "Montserrat", sans-serif;
    font-weight: 600;
    text-align: center;
    line-height: 1.15;
  }
  .front-name .line-main { display: block; font-size: 30px; letter-spacing: 1px; }
  .front-name .line-sub { display: block; font-size: 17px; letter-spacing: 7px; margin-top: 4px; }

  /* Back */
  .card-back {
    left: 540px; top: 500px;
    background: var(--card-white);
  }
  .back-name {
    position: absolute; left: 36px; top: 40px;
    font-family: "Montserrat", sans-serif;
    font-weight: 600;
    color: var(--brand-blue);
    line-height: 1.1;
  }
  .back-name .line-main { display: block; font-size: 27px; letter-spacing: .5px; }
  .back-name .line-sub { display: block; font-size: 16px; letter-spacing: 7px; margin-top: 4px; }
  .holder {
    position: absolute; right: 40px; top: 118px; text-align: right;
  }
  .holder-name {
    font-family: "Montserrat", sans-serif; font-weight: 500;
    font-size: 21px; color: var(--brand-blue); letter-spacing: .3px;
  }
  .holder-role { font-size: 13px; color: var(--ink-grey); margin-top: 3px; }
  .rule-holder {
    position: absolute; left: 36px; right: 40px; top: 150px;
    height: 1.5px; background: var(--rule-blue);
  }
  .rule-contact {
    position: absolute; left: 36px; width: 250px; top: 190px;
    height: 1.5px; background: var(--rule-blue);
  }
  .address {
    position: absolute; left: 36px; top: 200px;
    font-size: 13px; color: var(--ink-grey); line-height: 1.35;
  }
  .contacts {
    position: absolute; left: 36px; top: 240px; list-style: none;
    font-size: 13px; color: var(--ink-grey); line-height: 1.4;
  }
  .contacts li { display: flex; align-items: center; gap: 8px; }
  .contacts svg { width: 11px; height: 11px; fill: none; stroke: var(--icon-blue); stroke-width: 1.6; }
</style>
</head>
<body>
  <section class="card card-front" aria-label="Card front">
    <div class="front-mark"></div>
    <div class="front-name">
      <span class="line-main">KESTREL BUILDING</span>
      <span class="line-sub">SERVICES LTD</span>
    </div>
  </section>

  <section class="card card-back" aria-label="Card back">
    <div class="back-name">
      <span class="line-main">KESTREL BUILDING</span>
      <span class="line-sub">SERVICES LTD</span>
    </div>
    <div class="holder">
      <div class="holder-name">DANIEL HARPER</div>
    </div>
    <div class="rule-holder"></div>
    <div class="holder" style="top:156px"><div class="holder-role">Director</div></div>
    <div class="rule-contact"></div>
    <p class="address">18 Harbour Row<br>Wellington 6011</p>
    <ul class="contacts">
      <li><svg viewBox="0 0 12 12"><path d="M2 1.5l2 0 1 2.5-1.2 1a6 6 0 0 0 3.2 3.2l1-1.2 2.5 1v2a1 1 0 0 1-1 1A9 9 0 0 1 1 2.5a1 1 0 0 1 1-1z"/></svg>+64 21 555 0147</li>
      <li><svg viewBox="0 0 12 12"><rect x="2" y="4" width="8" height="6" rx="1"/><path d="M3.5 4V2h5v2"/></svg>+64 4 555 0182</li>
      <li><svg viewBox="0 0 12 12"><rect x="1" y="2.5" width="10" height="7" rx="1"/><path d="M1 3l5 4 5-4"/></svg>info@kestrelhub.co.nz</li>
      <li><svg viewBox="0 0 12 12"><circle cx="6" cy="6" r="4.8"/><path d="M1.2 6h9.6M6 1.2c2 2.4 2 7.2 0 9.6M6 1.2c-2 2.4-2 7.2 0 9.6"/></svg>www.kestrelhub.co.nz</li>
    </ul>
  </section>
</body>
</html>
```